tiling company needs letterhead urgent

We need a logo to represent our company on an electronic letterhead. We are a tiling firm called Corwell Tiling Ltd and undertake all aspects of tiling work. The final design of the logo should incorporate the type of work we do and should be modern. We do not want any designs which may be considered 'novelty' or 'cartoonish.' No characters please, we require something sleek and contemporary . Please ensure the company name is central to your design ,Corwell Tiling Ltd

Industry/Entity Type

Electronic

Requirements
Must have
• text on letterhead to included

Registered address 41 Birch lane Failsworth Manchester M359QT
Company number 5267093
VAT no 412957386
Mobile no 07831659047
Office no 0161 574 8192
Web :www.floorvane.co.uk
Email : gareth@floorvane.co.uk
Nice to have
• a tile theme

```html
<!DOCTYPE html>
<html lang="en">
<head>
<meta charset="utf-8">
<title>Corwell Tiling Ltd – Letterhead</title>
<link rel="stylesheet" href="https://fonts.googleapis.com/css2?family=Questrial&display=swap">
<style>
  :root {
    --backdrop: #e4e4e4;
    --paper: #ffffff;
    --brown: #4a3b26;
    --olive: #8f813b;
    --olive-light: #a89a4e;
    --muted: #d8d4c4;
  }
  * { margin: 0; padding: 0; box-sizing: border-box; }
  html, body {
    width: 1200px;
    height: 968px;
    overflow: hidden;
    background: var(--backdrop);
    font-family: "Questrial", "Century Gothic", sans-serif;
  }
  .letterhead {
    position: absolute;
    left: 282px;
    top: 26px;
    width: 636px;
    height: 900px;
    background: var(--paper);
    box-shadow: 0 6px 24px rgba(0,0,0,0.18);
  }
  .letterhead__header {
    position: absolute;
    top: 62px;
    left: 0;
    right: 0;
    text-align: center;
  }
  .brand {
    display: inline-flex;
    align-items: center;
    gap: 12px;
  }
  .brand__mark {
    width: 20px;
    height: 20px;
    background: var(--olive);
  }
  .brand__name {
    font-size: 34px;
    letter-spacing: 2px;
    color: var(--brown);
    text-transform: uppercase;
  }
  .brand__web {
    margin-top: 4px;
    font-size: 14px;
    color: var(--olive);
    letter-spacing: 0.5px;
  }
  .letterhead__footer {
    position: absolute;
    left: 0;
    right: 0;
    bottom: 0;
    height: 108px;
    background: var(--brown);
    border-top: 5px solid var(--olive);
    box-shadow: inset 0 5px 0 var(--paper);
    padding: 30px 36px 0;
    display: flex;
    justify-content: space-between;
    align-items: flex-start;
    font-size: 11.5px;
    line-height: 1.7;
  }
  .contact__address { color: #efe9d8; }
  .contact__label { color: var(--olive-light); }
  .contact__value { color: #efe9d8; }
  .footer__mark {
    width: 30px;
    height: 30px;
    margin-top: 6px;
    background: var(--olive);
    opacity: 0.8;
  }
  .registration {
    color: var(--olive-light);
    text-align: left;
  }
</style>
</head>
<body>
  <main class="letterhead">
    <header class="letterhead__header">
      <div class="brand">
        <span class="brand__mark"></span>
        <span class="brand__name">Corwell Tiling</span>
      </div>
      <div class="brand__web">www.floorvane.co.uk</div>
    </header>

    <footer class="letterhead__footer">
      <div class="contact">
        <div class="contact__address">41 Birch lane Failsworth Manchester M359QT</div>
        <div>
          <span class="contact__label">Mobile:</span> <span class="contact__value">07831659047</span> ·
          <span class="contact__label">Office:</span> <span class="contact__value">0161 574 8192</span> ·
          <span class="contact__label">Email:</span> <span class="contact__value">gareth@floorvane.co.uk</span>
        </div>
      </div>
      <span class="footer__mark"></span>
      <div class="registration">
        <div>VAT: 412957386</div>
        <div>Company number: 5267093</div>
      </div>
    </footer>
  </main>
</body>
</html>
```